Sleek, Professional Business Card Design Needed

Business Cards - Logo Attached.

We are a solar consulting company. We are national and want our cards to represent the professional high quality products that we offer.

Industry/Entity Type

Business

Contact Information for Business Card

n/a

Requirements
Must have
• Design
• Name
• Position
• Number
• Email
• Address
Should not have
• Not be too crowded

```html
<!DOCTYPE html>
<html lang="en">
<head>
<meta charset="utf-8">
<title>Bright Meridian Solar – Business Cards</title>
<link href="https://fonts.googleapis.com/css2?family=Montserrat:wght@300;400;600;700&display=swap" rel="stylesheet">
<style>
  :root {
    --page-bg: #e9e9e7;
    --card-dark: #232323;
    --card-light: #f7f7f8;
    --brand-blue: #1a8fd0;
    --brand-green: #8cc63f;
    --name-gray: #8b8b8b;
    --title-blue: #7fbde3;
    --divider-gray: #5b5b5b;
    --address-dark: #4a4a4a;
    --address-light: #2d2d2d;
  }
  * { box-sizing: border-box; margin: 0; padding: 0; }
  html, body {
    width: 1200px; height: 1200px; overflow: hidden;
    background: var(--page-bg);
    font-family: "Montserrat", sans-serif;
  }
  .sheet {
    width: 1200px; height: 1200px;
    display: flex; flex-direction: column; align-items: center; justify-content: center;
    gap: 70px;
  }
  .card {
    position: relative;
    width: 700px; height: 400px;
    border-radius: 6px;
    box-shadow: 0 10px 24px rgba(0,0,0,0.18);
  }
  .card--dark { background: var(--card-dark); }
  .card--light { background: var(--card-light); }

  .brand {
    position: absolute; left: 0; right: 0; top: 40px;
    display: flex; flex-direction: column; align-items: center; gap: 14px;
  }
  .brand__dot {
    width: 84px; height: 84px; border-radius: 50%;
    border: 8px solid var(--brand-green);
  }
  .brand__name {
    font-weight: 600; font-size: 34px; letter-spacing: 1px;
    color: var(--brand-blue); text-transform: uppercase;
  }
  .brand__rule {
    position: absolute; left: 170px; width: 380px; top: 206px;
    height: 3px; background: var(--brand-green);
  }

  .person {
    position: absolute; right: 370px; top: 226px; text-align: right;
  }
  .person__name { font-weight: 700; font-size: 23px; color: var(--name-gray); }
  .person__title {
    font-weight: 300; font-size: 21px; color: var(--title-blue); margin-top: 10px;
  }

  .divider {
    position: absolute; left: 346px; top: 228px; width: 5px; height: 130px;
    background: var(--divider-gray);
  }

  .contact {
    position: absolute; left: 374px; top: 228px;
    font-size: 17px; line-height: 25px; font-weight: 400;
  }
  .card--dark .contact__line { color: var(--address-dark); }
  .card--light .contact__line { color: var(--address-light); }
  .contact__link { color: var(--brand-blue); }
</style>
</head>
<body>
<main class="sheet">
  <section class="card card--dark">
    <div class="brand">
      <div class="brand__dot"></div>
      <div class="brand__name">Bright Meridian Solar</div>
    </div>
    <div class="brand__rule"></div>
    <div class="person">
      <div class="person__name">Name Firstname</div>
      <div class="person__title">Title</div>
    </div>
    <div class="divider"></div>
    <div class="contact">
      <div class="contact__line">Sunvale Partners inc</div>
      <div class="contact__line">88 Harbor Lane</div>
      <div class="contact__line">Suite 4 NY10020</div>
      <div class="contact__link">info@sunvale.com</div>
      <div class="contact__link">www.sunvale.com</div>
    </div>
  </section>

  <section class="card card--light">
    <div class="brand">
      <div class="brand__dot"></div>
      <div class="brand__name">Bright Meridian Solar</div>
    </div>
    <div class="brand__rule"></div>
    <div class="person">
      <div class="person__name">Name Firstname</div>
      <div class="person__title">Title</div>
    </div>
    <div class="divider"></div>
    <div class="contact">
      <div class="contact__line">Sunvale Partners inc</div>
      <div class="contact__line">88 Harbor Lane</div>
      <div class="contact__line">Suite 4 NY10020</div>
      <div class="contact__link">info@sunvale.com</div>
      <div class="contact__link">www.sunvale.com</div>
    </div>
  </section>
</main>
</body>
</html>
```